Book Cover Design - Uncovering Weight Loss Secrets

I need a book cover design for a book called 'Folding The Map'. It is a book that goes through all of the secrets to weight loss, without any crazy shakes or workouts or pills or potions. The book is really focused on helping people understand that Weight loss is simple and has more to do with our mindset as well as the food we were eating. It is about taking personal responsibility not looking for the next fancy revolutionary product that is going to help them magically melt the fat away. The book is pragmatic in nature and breaks down in simple terms how we can lose weight and keep it off for the rest of our lives. It shows the user that it is simple to lose weight, but it takes effort. They should stop looking for a quick fix when it comes to weight loss but instead eat healthy for the rest of their lives.
The book is intended to be hard-hitting no holds barred approach. The book has the same title as my business name. I will attach the current logo that we use in the business. This doesn't need to be on the front of the book maybe at the back down the bottom somewhere.
I am looking to have both an e-book cover and a standard printed book cover.
I don't have any colours in mind, my logo can be adapted to be different colours or just white.
The message that I am wanting people to feel when they see my book, is that all these Weightloss fads are a joke, that I know the secrets that will get them to their weight loss goal even if they fail at everything else before.
On the cover it should say the following.
FOLDING THE MAP
Uncovering the Weight Loss Secrets
The big companies have been trying to keep hidden for years!
COLIN MAYHEW
People who have failed many times trying to lose weight & need help
Weight Loss

```html
<!DOCTYPE html>
<html lang="en">
<head>
<meta charset="utf-8">
<title>Folding The Map – Cover Spread</title>
<link href="https://fonts.googleapis.com/css2?family=Playfair+Display:ital,wght@0,700;0,900;1,400&family=Roboto+Condensed:ital,wght@0,300;0,400;1,400&display=swap" rel="stylesheet">
<style>
  :root {
    --page: #ffffff;
    --paper-light: #ece4e2;
    --paper-mid: #ddd3d1;
    --paper-dark: #c9bdbb;
    --title-brown: #2e1a14;
    --subtitle-navy: #27305c;
    --band-purple: #545577;
    --band-text: #e3e2ee;
    --strip-grey: #cfcaca;
    --body-grey: #5e5656;
    --placeholder-text: #b9b2b2;
    --skin: #d9a99c;
    --figure-dark: #3a2520;
  }
  * { margin: 0; padding: 0; box-sizing: border-box; }
  html, body { width: 846px; height: 1200px; overflow: hidden; background: var(--page); }
  .canvas { position: relative; width: 846px; height: 1200px; }

  .spread {
    position: absolute; left: 46px; top: 346px;
    width: 754px; height: 508px;
    background: radial-gradient(ellipse at 40% 30%, var(--paper-light) 0%, var(--paper-mid) 65%, var(--paper-dark) 100%);
    overflow: hidden;
  }

  .back-cover { position: absolute; left: 0; top: 0; width: 357px; height: 508px; }
  .spine { position: absolute; left: 357px; top: 0; width: 37px; height: 508px; }
  .front-cover { position: absolute; left: 394px; top: 0; width: 360px; height: 508px; }

  .author-band {
    position: absolute; left: 357px; top: 0; width: 397px; height: 45px;
    background: var(--band-purple);
    font-family: "Roboto Condensed", sans-serif; font-weight: 300;
    color: var(--band-text); font-size: 20px; letter-spacing: 7px;
    line-height: 45px; padding-left: 138px; white-space: nowrap;
    z-index: 3;
  }

  /* title block */
  .title { position: absolute; left: 0; top: 0; width: 100%; height: 100%; z-index: 2;
    font-family: "Playfair Display", serif; font-weight: 900; color: var(--title-brown); }
  .title span { position: absolute; line-height: 1; white-space: nowrap;
    transform: scaleX(0.85); transform-origin: left top; }
  .title .big-line { letter-spacing: -1px; }

  .subtitle-line { position: absolute; z-index: 2; white-space: nowrap;
    font-family: "Playfair Display", serif; font-weight: 700; color: var(--subtitle-navy);
    border-left: 1px solid var(--body-grey); border-bottom: 3px solid var(--strip-grey); }
  .tagline { position: absolute; z-index: 2; font-family: "Roboto Condensed", sans-serif;
    font-style: italic; color: var(--subtitle-navy); }

  /* front */
  .front-cover .small-line { left: 24px; top: 62px; font-size: 31px; }
  .front-cover .line-the { left: 24px; top: 80px; font-size: 76px; }
  .front-cover .line-map { left: 24px; top: 139px; font-size: 76px; }
  .front-cover .subtitle-line { left: 23px; font-size: 15px; line-height: 18px; padding: 0 10px 0 4px; }
  .front-cover .sub-first { top: 224px; }
  .front-cover .sub-second { top: 247px; }
  .front-cover .tagline { left: 28px; top: 273px; font-size: 9.5px; line-height: 11px; width: 150px; }

  .cover-scene {
    position: absolute; left: 0; top: 200px; width: 360px; height: 308px; z-index: 1;
    background:
      radial-gradient(ellipse 72% 44% at 72% 115%, var(--skin) 0%, var(--skin) 96%, transparent 100%),
      radial-gradient(ellipse 26% 40% at 65% 36%, rgba(58,37,32,0.55) 0%, transparent 70%);
  }

  /* spine */
  .spine-title {
    position: absolute; left: 9px; top: 68px; white-space: nowrap;
    writing-mode: vertical-rl;
    font-family: "Playfair Display", serif; font-weight: 900;
    color: var(--title-brown); font-size: 17px; letter-spacing: 0.5px;
  }
  .spine-author {
    position: absolute; left: 0; top: 285px; width: 37px; height: 223px;
    background: var(--band-purple);
  }
  .spine-author span {
    position: absolute; left: 50%; top: 30px; transform: translateX(-50%);
    writing-mode: vertical-rl; white-space: nowrap; line-height: 1;
    font-family: "Roboto Condensed", sans-serif; font-weight: 300;
    color: var(--band-text); font-size: 16px; letter-spacing: 5px;
  }

  /* back */
  .back-cover .small-line { left: 42px; top: 25px; font-size: 21px; }
  .back-cover .line-the { left: 42px; top: 37px; font-size: 52px; }
  .back-cover .line-map { left: 42px; top: 78px; font-size: 52px; }
  .back-cover .subtitle-line { left: 42px; font-size: 10.5px; line-height: 13px; padding: 0 8px 0 3px; }
  .back-cover .sub-first { top: 137px; }
  .back-cover .sub-second { top: 154px; }
  .back-cover .tagline { left: 45px; top: 171px; font-size: 6.5px; line-height: 7.5px; width: 100px; }

  .blurb { position: absolute; left: 42px; top: 200px; width: 193px; z-index: 2;
    transform: scaleX(0.82); transform-origin: left top;
    font-family: "Roboto Condensed", sans-serif; font-weight: 300;
    color: var(--body-grey); font-size: 8.6px; line-height: 12px; }
  .blurb p + p { margin-top: 17px; }

  .author-photo {
    position: absolute; left: 42px; top: 401px; width: 52px; height: 62px;
    background: #f7f5f5; z-index: 2;
    font-family: "Roboto Condensed", sans-serif; font-weight: 300;
    color: var(--placeholder-text); font-size: 5.5px; line-height: 6.5px;
    padding: 24px 0 0 11px;
  }
  .back-author {
    position: absolute; left: 100px; top: 455px; z-index: 2; white-space: nowrap;
    font-family: "Roboto Condensed", sans-serif; font-weight: 300;
    color: #b9aeac; font-size: 6.5px; letter-spacing: 3px;
  }
  .back-scene {
    position: absolute; left: 0; top: 190px; width: 357px; height: 318px; z-index: 1;
    background:
      radial-gradient(ellipse 70% 40% at 55% 115%, rgba(201,160,150,0.45) 0%, rgba(201,160,150,0.45) 95%, transparent 100%),
      radial-gradient(ellipse 26% 42% at 60% 40%, rgba(58,37,32,0.12) 0%, transparent 70%);
  }
</style>
</head>
<body>
<div class="canvas">
  <section class="spread">

    <div class="back-cover">
      <div class="back-scene" role="img" aria-label="Faded repeat of the cover scene: two figures flying a kite on a rounded belly"></div>
      <h2 class="title">
        <span class="small-line">FOLDING</span>
        <span class="big-line line-the">THE</span>
        <span class="big-line line-map">MAP</span>
      </h2>
      <p class="subtitle-line sub-first">Uncovering</p>
      <p class="subtitle-line sub-second">the Weight Loss Secrets</p>
      <p class="tagline">The big companies have been trying to keep hidden for years!</p>
      <div class="blurb">
        <p>uncovering the weight loss secrets The big companies have been trying to keep hidden for years! uncovering the weight loss secrets The big companies have been trying to keep hidden for years! uncovering the weight loss secrets The big companies have been trying to keep hidden for years! uncovering the weight loss secrets The big companies have been trying to keep hidden for years! uncovering the weight loss secrets The big companies have been trying to keep hidden for years!</p>
        <p>uncovering the weight loss secrets The big companies have been trying to keep hidden for years! uncovering the weight loss secrets The big companies have been trying to keep hidden for years! uncovering the weight loss secrets The big companies have been trying to keep hidden for years!</p>
      </div>
      <div class="author-photo" role="img" aria-label="Author photograph">Author<br>photograph</div>
      <p class="back-author">COLIN MAYHEW</p>
    </div>

    <div class="spine">
      <p class="spine-title">FOLDING THE MAP</p>
      <div class="spine-author"><span>COLIN MAYHEW</span></div>
    </div>

    <div class="author-band">COLIN&nbsp;&nbsp;MAYHEW</div>

    <div class="front-cover">
      <div class="cover-scene" role="img" aria-label="Silhouettes of an adult and a child flying a kite, standing on a rounded bare belly"></div>
      <h1 class="title">
        <span class="small-line">FOLDING</span>
        <span class="big-line line-the">THE</span>
        <span class="big-line line-map">MAP</span>
      </h1>
      <p class="subtitle-line sub-first">Uncovering</p>
      <p class="subtitle-line sub-second">the Weight Loss Secrets</p>
      <p class="tagline">The big companies have been trying to keep hidden for years!</p>
    </div>

  </section>
</div>
</body>
</html>
```